business card design and letterhead for a building inspection company. We have a pre-purchase building and pest inspection ( i inspect house before people purchase it)
Updates

Linda has been so so responsive and good, i highly recommend her

Industry/Entity Type

Building

Contact Information for Business Card

audience, solicitor, real estate agent, mortgage brokerthe rest of the info will be in the attachement business card

```html
<!DOCTYPE html>
<html lang="en">
<head>
<meta charset="utf-8">
<title>Keystone Inspections – Business Card</title>
<link href="https://fonts.googleapis.com/css2?family=Open+Sans:wght@400;600;700&display=swap" rel="stylesheet">
<style>
  :root {
    --brand-blue: #1a78c2;
    --ink: #3a3a3a;
    --ink-dark: #111111;
    --card-top: #ffffff;
    --card-bottom: #e6e7e9;
    --backdrop: #d9d6d0;
    --white: #ffffff;
  }
  * { margin: 0; padding: 0; box-sizing: border-box; }
  html, body {
    width: 1200px; height: 800px; overflow: hidden;
    background: var(--backdrop);
    font-family: "Open Sans", Arial, sans-serif;
  }
  .card {
    position: absolute; left: 75px; top: 100px;
    width: 1050px; height: 600px;
    background: radial-gradient(ellipse at 60% 40%, var(--card-top) 0%, var(--card-bottom) 100%);
    box-shadow: 0 12px 30px rgba(0,0,0,0.18);
    overflow: hidden;
  }
  .card__swoosh { position: absolute; inset: 0; width: 100%; height: 100%; }
  .brand {
    position: absolute; left: 70px; top: 150px;
    display: flex; align-items: center; gap: 14px;
  }
  .brand__mark { width: 34px; height: 34px; background: var(--brand-blue); }
  .brand__name {
    font-size: 40px; font-weight: 700; color: var(--brand-blue);
    letter-spacing: 0.5px;
  }
  .person { position: absolute; right: 70px; top: 45px; text-align: right; }
  .person__name { font-size: 34px; font-weight: 700; color: var(--brand-blue); line-height: 1.15; }
  .person__title { font-size: 25px; color: var(--ink); }
  .address {
    position: absolute; right: 70px; top: 200px; text-align: right;
    font-size: 24px; line-height: 1.6; color: var(--ink);
  }
  .contacts {
    position: absolute; left: 70px; top: 330px;
    list-style: none; font-size: 23px; color: var(--ink); line-height: 1.65;
  }
  .contacts li { display: flex; align-items: center; gap: 16px; }
  .contacts svg { width: 22px; height: 22px; fill: var(--brand-blue); flex: none; }
  .website {
    position: absolute; right: 55px; bottom: 120px;
    font-size: 32px; color: var(--white);
  }
  .website strong { font-weight: 700; }
</style>
</head>
<body>
  <article class="card">
    <svg class="card__swoosh" viewBox="0 0 1050 600" preserveAspectRatio="none" aria-hidden="true">
      <path d="M70 600 Q 520 420 1050 325 L1050 338 Q 540 440 130 600 Z" fill="var(--ink-dark)"/>
      <path d="M150 600 Q 580 450 1050 345 L1050 600 Z" fill="var(--brand-blue)"/>
    </svg>

    <div class="brand">
      <span class="brand__mark"></span>
      <span class="brand__name">Keystone Inspections</span>
    </div>

    <div class="person">
      <p class="person__name">Daniel Whitford</p>
      <p class="person__title">Managing Director</p>
    </div>

    <address class="address" style="font-style:normal">
      Harbor Ridge LLC<br>
      418 Maple Avenue, Suite 310<br>
      Riverton, PA 19876
    </address>

    <ul class="contacts">
      <li>
        <svg viewBox="0 0 24 24"><path d="M7 1h10a2 2 0 0 1 2 2v18a2 2 0 0 1-2 2H7a2 2 0 0 1-2-2V3a2 2 0 0 1 2-2zm0 3v14h10V4zm5 15.5a1.2 1.2 0 1 0 0 2.4 1.2 1.2 0 0 0 0-2.4z"/></svg>
        555.210.4471
      </li>
      <li>
        <svg viewBox="0 0 24 24"><path d="M6 2h9l3 3v5H6zM3 11h18a2 2 0 0 1 2 2v8H1v-8a2 2 0 0 1 2-2zm3 4v2h3v-2zm5 0v2h3v-2z"/></svg>
        555.318.2290
      </li>
      <li>
        <svg viewBox="0 0 24 24"><path d="M2 8c3-3 17-3 20 0l-1 4-4-1v-2c-3-1-7-1-10 0v2l-4 1zM6 13h12l3 8H3zm6 2a2.5 2.5 0 1 0 0 5 2.5 2.5 0 0 0 0-5z"/></svg>
        555.406.7735
      </li>
      <li>
        <svg viewBox="0 0 24 24"><path d="M2 5h20v14H2zm2 2v.5l8 5 8-5V7zm0 3v7h16v-7l-8 5z"/></svg>
        hello@keystonecheck.com
      </li>
    </ul>

    <p class="website">www.<strong>keystonecheck</strong>.com</p>
  </article>
</body>
</html>
```